DELVANE ROOFING YARD SIGN

We need a yard sign to put in our customers' yards when we are roofing their home.
Delvane Roofing
468 Pettigrew Rd
Harlow Bend MS 39452
phone: 555-555-0148

Maybe some verbiage like "Your Hometown Roofing Experts"
or
"Family Owned Since 1962"

```html
<!DOCTYPE html>
<html lang="en">
<head>
<meta charset="UTF-8">
<title>Delvane Roofing Yard Sign</title>
<link rel="stylesheet" href="https://fonts.googleapis.com/css2?family=Playfair+Display:wght@700;900&display=swap">
<style>
  :root {
    --ink: #0a0a0a;
    --paper: #ffffff;
    --ring: #9a9a9a;
  }
  html, body {
    margin: 0;
    padding: 0;
    width: 1200px;
    height: 900px;
    overflow: hidden;
    background: var(--paper);
  }
  .yard-sign {
    display: block;
    width: 1200px;
    height: 900px;
    font-family: "Playfair Display", Georgia, serif;
    font-variant-numeric: lining-nums;
  }
  .headline { fill: var(--ink); font-weight: 900; }
  .tagline { fill: var(--ink); font-weight: 700; }
  .logo-name { fill: var(--ink); font-weight: 900; }
  .address { fill: var(--paper); font-weight: 700; }
  .phone { fill: var(--paper); font-weight: 900; }
</style>
</head>
<body>
<svg class="yard-sign" viewBox="0 0 1200 900" xmlns="http://www.w3.org/2000/svg">
  <defs>
    <linearGradient id="roof-tone" x1="0" y1="0" x2="0" y2="1">
      <stop offset="0" stop-color="#ffffff"/>
      <stop offset="0.3" stop-color="#f2f2f2"/>
      <stop offset="0.45" stop-color="#c9cbcb"/>
      <stop offset="0.62" stop-color="#8a8c8c"/>
      <stop offset="0.74" stop-color="#6a6c6c"/>
      <stop offset="0.82" stop-color="#2a2a2a"/>
      <stop offset="0.88" stop-color="#000000"/>
      <stop offset="1" stop-color="#000000"/>
    </linearGradient>
  </defs>

  <rect class="roof-backdrop" x="0" y="0" width="1200" height="900" fill="url(#roof-tone)"
        role="img" aria-label="Close-up photograph of grey metal roof tiles fading into a dark base"/>

  <g class="logo-seal">
    <circle cx="250" cy="240" r="232" fill="var(--paper)" stroke="var(--ring)" stroke-width="5"/>
    <text class="logo-name" x="250" y="232" text-anchor="middle" font-size="50">DELVANE</text>
    <text class="logo-name" x="250" y="290" text-anchor="middle" font-size="50">ROOFING</text>
  </g>

  <g class="headline-block">
    <text class="headline" x="456" y="98" font-size="96" textLength="724" lengthAdjust="spacingAndGlyphs">YOUR HOMETOWN</text>
    <text class="headline" x="529" y="200" font-size="103" textLength="589" lengthAdjust="spacingAndGlyphs">ROOFING</text>
    <text class="headline" x="523" y="342" font-size="154" textLength="643" lengthAdjust="spacingAndGlyphs">EXPERTS</text>
    <text class="tagline" x="551" y="437" font-size="50" textLength="564" lengthAdjust="spacingAndGlyphs">FAMILY OWNED SINCE 1962</text>
  </g>

  <g class="contact-band">
    <text class="address" x="33" y="803" font-size="32" textLength="262" lengthAdjust="spacingAndGlyphs">DELVANE ROOFING</text>
    <text class="address" x="33" y="838" font-size="32" textLength="240" lengthAdjust="spacingAndGlyphs">468 PETTIGREW RD</text>
    <text class="address" x="33" y="873" font-size="32" textLength="374" lengthAdjust="spacingAndGlyphs">HARLOW BEND MS 39452</text>
    <text class="phone" x="458" y="873" font-size="115" textLength="717" lengthAdjust="spacingAndGlyphs">555-555-0148</text>
  </g>
</svg>
</body>
</html>
```